Bodywork Quietude Business Card Design

I want to create a very elegant and sophisticated two sided business card for my massage practice (www.bodyworkquietude.net). I have attached the logo and a PDF with some ideas down for the back of the card but I am open to suggestions. I will want to tie in a post card and flyer to the card later.
Similar colors to website would be great.
Target Market(s)
High end clientele, people looking for a sophisticated spa experience.
Industry/Entity Type
Massage
Contact Information for Business Card
Bodywork Quietude
7318 Larkspur Ave S, Suite 305
Seattle, WA 98103
(206) 555-0147
www.bodyworkquietude.net
Look and feel

```html
<!DOCTYPE html>
<html lang="en">
<head>
<meta charset="utf-8">
<title>Bodywork Quietude – Business Card</title>
<link href="https://fonts.googleapis.com/css2?family=Lora:wght@400;500&family=Marcellus+SC&family=Exo+2:wght@300;400&display=swap" rel="stylesheet">
<style>
  :root{
    --backdrop:#e9e9eb;
    --card-black:#111112;
    --card-black-edge:#1c1c1e;
    --ink-white:#f4f4f4;
    --ink-navy:#1d2b3a;
    --band-blue:#0c7fc4;
    --band-blue-deep:#0a6aa6;
    --band-gold:#f2b21c;
    --paper:#ffffff;
  }
  *{box-sizing:border-box;margin:0;padding:0}
  html,body{width:1200px;height:694px;overflow:hidden}
  body{background:var(--backdrop);position:relative;font-family:"Lora",serif}

  .card{position:absolute;top:192px;width:540px;height:309px;border-radius:3px;overflow:hidden;
        box-shadow:0 6px 18px rgba(0,0,0,.18)}

  /* front */
  .card--front{left:40px;background:radial-gradient(ellipse at 55% 30%,var(--card-black-edge),var(--card-black) 70%);
               color:var(--ink-white);text-align:center}
  .brand{display:flex;align-items:center;justify-content:center;gap:10px;margin-top:58px}
  .brand__dot{width:12px;height:12px;border-radius:50%;background:currentColor}
  .brand__name{font-family:"Lora",serif;font-size:24px;font-weight:400;letter-spacing:1px}
  .front__pitch{margin:44px auto 0;width:440px;font-size:18px;line-height:1.3;font-weight:400}
  .front__service{margin-top:26px;font-family:"Marcellus SC",serif;font-size:19px;letter-spacing:1.5px}

  /* back */
  .card--back{left:620px;background:var(--paper)}
  .card--back .brand{color:var(--ink-navy);margin-top:44px;justify-content:flex-start;padding-left:120px}
  .band{position:absolute;left:0;right:0;top:140px;height:122px;
        background:linear-gradient(100deg,var(--band-blue-deep),var(--band-blue) 45%,var(--band-blue));
        border-top:3px solid var(--band-gold)}
  .band__notch{position:absolute;top:-1px;left:376px;width:0;height:0;
        border-left:7px solid transparent;border-right:7px solid transparent;border-top:8px solid var(--band-gold)}
  .band__texture{position:absolute;left:180px;top:0;width:260px;height:100%;
        background:radial-gradient(ellipse at center,rgba(255,255,255,.14),rgba(255,255,255,0) 70%)}
  .band__title{position:absolute;right:24px;top:10px;font-family:"Exo 2",sans-serif;font-weight:300;
        font-size:19px;color:var(--paper)}
  .contacts{position:absolute;left:24px;top:34px;list-style:none;font-family:"Exo 2",sans-serif;
        font-weight:300;font-size:14px;color:var(--paper)}
  .contacts li{display:flex;align-items:center;gap:9px;height:21px}
  .contacts svg{width:13px;height:13px;fill:none;stroke:var(--paper);stroke-width:1.6}
  .address{position:absolute;left:0;right:0;bottom:14px;text-align:center;font-family:"Lora",serif;
        font-size:17px;color:#111}
</style>
</head>
<body>

<section class="card card--front">
  <div class="brand"><span class="brand__dot"></span><span class="brand__name">Bodywork Quietude</span></div>
  <p class="front__pitch">Come and Experience the Most Relaxing and Invitingly Deep Massage of Your Life.....</p>
  <p class="front__service">Deep Lomi Ultra Relaxation Massage</p>
</section>

<section class="card card--back">
  <div class="brand"><span class="brand__dot"></span><span class="brand__name">Bodywork Quietude</span></div>
  <div class="band">
    <span class="band__notch"></span>
    <div class="band__texture" role="img" aria-label="Soft honeycomb texture on the blue band"></div>
    <p class="band__title">Bodywork Quietude</p>
    <ul class="contacts">
      <li><svg viewBox="0 0 14 14"><path d="M2 4c0-2 3-2 5-2s5 0 5 2l-2 1-1-1H5L4 5z M3 7h8l1 5H2z"/></svg>(206) 555-0147</li>
      <li><svg viewBox="0 0 14 14"><rect x="2" y="5" width="10" height="7"/><rect x="4" y="2" width="6" height="3"/></svg>000-111-2222</li>
      <li><svg viewBox="0 0 14 14"><rect x="1.5" y="3.5" width="11" height="8"/><path d="M1.5 3.5l5.5 5 5.5-5"/></svg>support@bodyworkquietude.net</li>
      <li><svg viewBox="0 0 14 14"><circle cx="7" cy="7" r="5.5"/><ellipse cx="7" cy="7" rx="2.3" ry="5.5"/><path d="M1.5 7h11"/></svg>www.bodyworkquietude.net</li>
    </ul>
  </div>
  <p class="address">7318 Larkspur Ave S, Suite 305 Seattle, WA 98103</p>
</section>

</body>
</html>
```